Create a web design for a vehicle codes lookup website

Create a bright and fun web design to replace our current boring one!

-Make a new design for this page that shows vehicle codes information: http://plinkor.net/vin/mara-dulek.4182.html
-Click "Random VIN" to see more examples.
-The page shows the vehicle information (see above example) is the most important one to add a redesign to. Bonus points if you create a redesign for the main page as well: plinkor.net.

Number of Pages Required

2 page

Requirements
Must have
• Be fun and have bright colors!
Should not have
• Do not add pictures of specific people or vehicles unless they can be used on every page. The example page has a Brevik Solano, but do not add a picture of the Brevik Solano because other pages have different vehicles.

```html
<!DOCTYPE html>
<html lang="en">
<head>
<meta charset="utf-8">
<title>Vehicle Purchase Information</title>
<link href="https://fonts.googleapis.com/css2?family=Open+Sans:wght@400;600;700&display=swap" rel="stylesheet">
<style>
:root{--blue:#1f5fc0;--ink:#333;--muted:#777;--line:#e3e6eb;--row:#f4f6f9;--bg:#eef0f3;--white:#fff}
*{box-sizing:border-box;margin:0;padding:0}
html,body{width:730px;height:1200px;overflow:hidden}
body{background:var(--bg);font-family:"Open Sans",Arial,sans-serif;color:var(--ink);font-size:5.5px}
.topbar{height:45px;background:var(--white);display:flex;align-items:center;padding:0 50px}
.brand{display:flex;align-items:center;gap:8px}
.brand-mark{width:24px;height:24px;background:var(--blue);border-radius:3px}
.brand-vin{font-size:10px;font-weight:700;color:var(--blue);letter-spacing:.3px}
.brand-sub{font-size:7px;font-weight:700;color:var(--blue)}
.social{margin-left:auto;display:flex;gap:4px}
.social span{width:12px;height:12px;background:var(--blue);border-radius:2px}
.nav{height:17px;background:var(--blue);display:flex;align-items:center;padding:0 56px;gap:26px}
.nav a{color:var(--white);font-size:5.5px;text-decoration:none}
.card{margin:10px 50px 0;background:var(--white);height:1040px;padding:12px 20px}
h2{font-size:6.5px;font-weight:700;margin-bottom:3px}
.owner{color:var(--blue);font-weight:700;font-size:6.5px;margin-bottom:10px}
.specs{display:grid;grid-template-columns:1fr 1fr;column-gap:18px;border-top:1px solid var(--line)}
.spec{display:flex;align-items:center;height:18px;border-bottom:1px solid var(--line);padding-left:4px}
.spec:nth-child(4n+1),.spec:nth-child(4n+2){background:var(--row)}
.ico{width:6px;height:6px;border-radius:50%;background:var(--blue);margin-right:7px;flex:none}
.spec .k{width:68px;color:var(--muted)}
.spec .v{color:var(--ink)}
.fuel-title{margin:52px 0 14px}
.fuel{border-top:1px solid var(--line)}
.frow{display:flex;align-items:center;height:34.5px;border-bottom:1px solid var(--line);padding-left:6px}
.frow:nth-child(odd){background:var(--row)}
.frow .k{width:58px;color:var(--muted)}
.frow .v{width:84px;font-weight:600}
.frow .d{color:var(--muted);flex:1;padding-right:10px;line-height:1.4}
.frow .d a{color:var(--blue);font-weight:600;text-decoration:none}
.footer{margin:8px 50px 0;height:30px;background:var(--blue);display:flex;flex-direction:column;align-items:center;justify-content:center;gap:6px}
.footer nav{display:flex;gap:10px}
.footer a,.footer p{color:var(--white);font-size:5px;text-decoration:none}
</style>
</head>
<body>
<header class="topbar">
  <div class="brand">
    <div class="brand-mark"></div>
    <div><div class="brand-vin">4B7KX52R918304627</div><div class="brand-sub">VEHICLE PURCHASE INFORMATION</div></div>
  </div>
  <div class="social"><span></span><span></span><span></span></div>
</header>
<nav class="nav"><a href="#">Home</a><a href="#">Search by owner</a><a href="#">VIN Lookup</a><a href="#">Complete List</a><a href="#">Contact Us</a><a href="#">Random VIN</a></nav>

<main class="card">
  <h2>Customer Name</h2>
  <p class="owner">MARA DULEK</p>
  <section class="specs">
    <div class="spec"><i class="ico"></i><span class="k">Address</span><span class="v">4418 Harbor Ln</span></div>
    <div class="spec"><i class="ico"></i><span class="k">Steering Type</span><span class="v">RNP</span></div>
    <div class="spec"><i class="ico"></i><span class="k">City</span><span class="v">Ferndale</span></div>
    <div class="spec"><i class="ico"></i><span class="k">Antibrake system</span><span class="v">4-Wheel ABS</span></div>
    <div class="spec"><i class="ico"></i><span class="k">State</span><span class="v">WA</span></div>
    <div class="spec"><i class="ico"></i><span class="k">Tank Size</span><span class="v">18.00 gallon</span></div>
    <div class="spec"><i class="ico"></i><span class="k">Zip</span><span class="v">98211-4470</span></div>
    <div class="spec"><i class="ico"></i><span class="k">Overall Height</span><span class="v">49.10 in</span></div>
    <div class="spec"><i class="ico"></i><span class="k">Year</span><span class="v">2007</span></div>
    <div class="spec"><i class="ico"></i><span class="k">Overall Length</span><span class="v">175.60 in</span></div>
    <div class="spec"><i class="ico"></i><span class="k">Make</span><span class="v">BREVIK</span></div>
    <div class="spec"><i class="ico"></i><span class="k">Overall Width</span><span class="v">72.60 in</span></div>
    <div class="spec"><i class="ico"></i><span class="k">Model</span><span class="v">SOLANO</span></div>
    <div class="spec"><i class="ico"></i><span class="k">Standard Seating</span><span class="v">2</span></div>
    <div class="spec"><i class="ico"></i><span class="k">VIN</span><span class="v">4B7KX52R918304627</span></div>
    <div class="spec"><i class="ico"></i><span class="k">Optional Seating</span><span class="v">No data</span></div>
    <div class="spec"><i class="ico"></i><span class="k">Trim Level</span><span class="v">Convertible 2D</span></div>
    <div class="spec"><i class="ico"></i><span class="k">Highway Mileage</span><span class="v">27 - 28 miles/gallon</span></div>
    <div class="spec"><i class="ico"></i><span class="k">Engine</span><span class="v">6.0L V8 OHV 16V</span></div>
    <div class="spec"><i class="ico"></i><span class="k">City Mileage</span><span class="v">17 - 18 miles/gallon</span></div>
    <div class="spec"><i class="ico"></i><span class="k">Made in</span><span class="v">UNITED STATES</span></div>
    <div class="spec"><i class="ico"></i><span class="k">Transmission</span><span class="v">6-Speed Automatic | 6-Speed Manual</span></div>
  </section>

  <h2 class="fuel-title">US Dept of Energy Fuel Economy Information</h2>
  <section class="fuel">
    <div class="frow"><span class="k">Barrels 08</span><span class="v">17.347056000002</span><span class="d">Annual petroleum consumption in barrels for regular fuel (all gallons)</span></div>
    <div class="frow"><span class="k">City 08</span><span class="v">16</span><span class="d">City MPG for regular fuel</span></div>
    <div class="frow"><span class="k">CO 2</span><span class="v">-1</span><span class="d">Tailpipe CO2 in grams/mile for regular fuel</span></div>
    <div class="frow"><span class="k">CO 2 A</span><span class="v">-1</span><span class="d">Tailpipe CO2 in grams/mile for alternative fuel</span></div>
    <div class="frow"><span class="k">CO2 Tailpipe GPM</span><span class="v">467.736842105263</span><span class="d">Tailpipe CO2 in grams/mile for regular fuel</span></div>
    <div class="frow"><span class="k">Combined 08</span><span class="v">19</span><span class="d">Combined MPG for regular fuel</span></div>
    <div class="frow"><span class="k">Cylinders</span><span class="v">8</span><span class="d">Engine cylinders</span></div>
    <div class="frow"><span class="k">Displacement</span><span class="v">6.0</span><span class="d">Engine displacement in liters</span></div>
    <div class="frow"><span class="k">fe Score</span><span class="v">-1</span><span class="d">EPA Fuel Economy Score (-1 = Not available)</span></div>
    <div class="frow"><span class="k">Fuel Cost 08</span><span class="v">1950</span><span class="d">Annual fuel cost for regular fuel based on 15,000 miles, 55% city driving, and the price of fuel used by the vehicle</span></div>
    <div class="frow"><span class="k">ghg Score</span><span class="v">-1</span><span class="d">EPA GHG score (-1 = Not available)</span></div>
    <div class="frow"><span class="k">ghg Score A</span><span class="v">-1</span><span class="d">EPA GHG score for dual fuel vehicle running on the alternative fuel (-1 = Not available)</span></div>
    <div class="frow"><span class="k">Highway 08</span><span class="v">24</span><span class="d">Highway MPG for regular fuel</span></div>
    <div class="frow"><span class="k">ID</span><span class="v">23444</span><span class="d">Vehicle record ID</span></div>
    <div class="frow"><span class="k">U City</span><span class="v">19.6</span><span class="d">Unadjusted city MPG for regular fuel, see the description of the EPA test procedures</span></div>
    <div class="frow"><span class="k">U Highway</span><span class="v">34.4</span><span class="d">Unadjusted highway MPG for regular fuel, see the description of the EPA test procedures</span></div>
    <div class="frow"><span class="k">Year</span><span class="v">2007</span><span class="d">Model year</span></div>
    <div class="frow"><span class="k">Save Spend</span><span class="v">-3250</span><span class="d">You save/spend over 5 years compared to an average car. Savings are positive; a greater amount spent yields a negative number. For dual fuel vehicles, this is the cost savings for gasoline</span></div>
    <div class="frow"><span class="k">Court Records Search</span><span class="v">MARA DULEK</span><span class="d"><a href="#">Click to run a court records search for MARA DULEK</a></span></div>
    <div class="frow"><span class="k">VIN Lookup</span><span class="v">4B7KX52R918304627</span><span class="d"><a href="#">Click to run a vehicle lookup for VIN 4B7KX52R918304627</a></span></div>
  </section>
</main>

<footer class="footer">
  <nav><a href="#">Home</a><a href="#">Search by owner</a><a href="#">VIN Lookup</a><a href="#">Complete List</a><a href="#">Contact Us</a><a href="#">Random VIN</a></nav>
  <p>PRIVACY POLICY &nbsp;|&nbsp; © Copyright 2015 plinkor.net</p>
</footer>
</body>
</html>
```